●お仕事の概要● インターネット上で通販印刷「カミナル。」を運営している「株式会社ソラテック」と申します。 カミナル。 http://www.kaminaru-example.jp/ 今回の依頼は、名刺印刷「カミナル。」(http://www.kaminaru-example.jp/)で使用する【ハンドメイド台紙のデザイン】 を募集いたします。 募集したデザインは弊社サイトカミナル。「デザインを選んで名刺を作成」の「ハンドメイド台紙」として使用します。 https://kaminaru-example.jp/design-order/ *古くからのデザインを掲載しておりますので、スタイリッシュで様々なシーンに使用できるデザインに 一新したいと考えております。 デザインの参考イメージは添付ファイル内「reference」フォルダ内に入れております。 ハンドメイド台紙とは、ハンドメイド用品(主にアクセサリー等)を売る時につける台紙です。 *「参考画像1」をご確認ください。 提案をお願いしたいデザインは4種類です。どのデザインで提案いただきましても問題ありません。 *「参考画像2」をご確認ください。 *背景が色ベタになっているイメージ画像ありますが、ベタ面は印刷時にムラが発生しやすいため 少ない方が好ましいです。 また今回も*複数採用*の募集となります。 契約成立の金額は下記金額となります。 上位 1位 5,000円(1点) 2位 3,000円(1点) その他 採用デザイン 1点:1,000円 (合計 20点ほどを予定しております。) 全応募デザインより弊社スタッフにてランク付けさせて頂き、上位1位の方には5千円、以下3,000円〜1,000円迄の報酬となります。 ※クオリティーなどにより20件未満の契約となる場合がございます ※逆によいデザインが沢山ある場合は20件以上採用いたします ●作成デザイン詳細● ※デザイン作成のときはテンプレート(添付ファイル)の使用をお願いします 1.ファイル形式 「ai」または「psd」形式 2.作成サイズ 名刺サイズ(91mm×55mmに上下左右3mmの塗り足し、つまり97mm×61mm) ※縦横どちらでも構いません ※psdファイルの場合は解像度350dpi、RGB形式でお願いします ※デザイン作成のときはテンプレート(添付ファイル)の使用をお願いします 3.作成デザインについて 【ハンドメイド台紙】を募集いたします。 今回仮で入れていただく内容は、お客様によって入力内容が異なりますので、入力内容に左右されないデザインを意識して作成お願いします。 *色ベタは印刷時にムラが発生しやすいため少ない方が好ましいです。 *グラデーションは印刷のムラが出やすいので、大きい面での使用を控えていただきたいです。 *枠がついているデザインは、断裁がズレた場合目立ちますので、枠なしの方が好ましいです。 4.お客様が編集する下記文面を仮でいれてください。 ・「shop name」 ・「handmade design」 雰囲気については、添付ファイルの「reference」内のデザインをご確認ください。 ・レイアウト、フォント変更OK 文字の大きさについて:特に制限はありませんが、変形文字などはNGとなります。 5.文字の控えについて ・印刷で切れてはいけない重要なデザインは85mm×49mm内に配置してください 6.納品時の注意点 ・aiデータの場合は「アウトライン化済み」「アウトライン化なし」のデータ両方の納品をお願いします ・psdデータの場合はレイヤーは統合せずに分けた状態での納品をお願いします 7.その他、デザイン作成においての注意点はテンプレートを参考にしてください ●重要視する点・経験● ・コンセプト(3.作成デザインについて)にそった的確なデザイン提案をしてくださる方 ・クライアント企業とのコミュニケーションに慣れており、細かい修正依頼にも対応いただける方 ●注意点・禁止事項● ※デザインはオリジナルのもののみとします。 ※ワークモールの規約により、採用作品の著作権は納品・契約完了後は当社が所有することになります。 ※採用作品の販売・使用・公表の権利は弊社のものとさせて頂き、弊社サイト(カミナル。)上での商用利用に使用させて頂きます。 ※契約が成立した場合でも、盗作等が発覚した場合や他でも同じデザインが使用されている等が発覚した場合は契約を破棄させて頂きます。 では皆様のご応募お待ちしております。 |
採用の理由
シンプルでありながらも おしゃれな雰囲気が社内で人気でしたので、
こちらのデザインを採用とさせていただきます。ステキなご提案をありがとうございました。
応募者全員へのお礼・コメント
皆様、この度のコンペにもたくさんのご提案をありがとうございました。
ハンドメイドカードは弊社初の試みでしたが、ステキなデザインを多数ご提案いただき
サイトオープンが待ち遠しいものとなりました。
また機会がございましたらコンペを行いますので、ご協力をいただけましたら幸いです。

```html
<!DOCTYPE html>
<html lang="en">
<head>
<meta charset="utf-8">
<title>Shop Name – Handmade Accessories Card</title>
<link href="https://fonts.googleapis.com/css2?family=Quicksand:wght@400;500&display=swap" rel="stylesheet">
<style>
  :root {
    --paper: #ffffff;
    --backing-tone: #e3e1d8;
    --badge-green: #4d8a6b;
    --wreath-tone: #76a98d;
    --ribbon-gold: #b99c5e;
    --text-light: #ffffff;
  }
  html, body {
    margin: 0;
    padding: 0;
    overflow: hidden;
    background: var(--paper);
  }
  .card {
    position: relative;
    width: 811px;
    height: 1200px;
    overflow: hidden;
    background: var(--paper);
    font-family: "Quicksand", sans-serif;
  }
  .card__backing {
    position: absolute;
    left: 0;
    top: 206px;
    width: 100%;
    height: 994px;
    background: var(--backing-tone);
  }
  .badge {
    position: absolute;
    left: 0;
    top: 0;
    width: 811px;
    height: 480px;
  }
  .badge__title {
    font-family: "Quicksand", sans-serif;
    font-weight: 500;
    font-size: 54px;
    fill: var(--text-light);
  }
  .badge__subtitle {
    font-family: "Quicksand", sans-serif;
    font-weight: 400;
    font-size: 24px;
    fill: var(--text-light);
  }
</style>
</head>
<body>
  <main class="card">
    <div class="card__backing" role="img" aria-label="Soft beige vertical stripe pattern covering the card backing"></div>

    <svg class="badge" viewBox="0 0 811 480" xmlns="http://www.w3.org/2000/svg">
      <g class="badge__ribbon" role="img" aria-label="Gold ribbon tie hanging the tag">
        <path d="M378 0 L398 68 L412 68 L400 0 Z" fill="var(--ribbon-gold)"/>
        <path d="M430 0 L412 68 L424 68 L448 0 Z" fill="var(--ribbon-gold)"/>
        <circle cx="410" cy="68" r="12" fill="var(--ribbon-gold)"/>
      </g>

      <circle class="badge__disc" cx="397" cy="262" r="190" fill="var(--badge-green)"/>
      <circle class="badge__wreath" cx="397" cy="262" r="152" fill="none"
              stroke="var(--wreath-tone)" stroke-width="40"
              role="img" aria-label="Ring of white leaves and gold dots and sprigs circling the shop name"/>

      <text class="badge__title" x="400" y="227" text-anchor="middle">Shop</text>
      <text class="badge__title" x="400" y="288" text-anchor="middle">Name</text>
      <line class="badge__rule" x1="300" y1="302" x2="490" y2="302"
            stroke="var(--text-light)" stroke-width="1.5"/>
      <text class="badge__subtitle" x="400" y="333" text-anchor="middle">Handmade</text>
      <text class="badge__subtitle" x="400" y="361" text-anchor="middle">Accessories</text>
    </svg>
  </main>
</body>
</html>
```